The logo name is "Harbon Vellis". The name of the product will be "Tavoren Calm". This product is specifically formulated for amputees. Therefore under the product name it should state "for amputees". The catch phrase will be "Experience Harbon gain Wellstride"
These are the things we need on the label:
Logo, product name, "for amputees", "Experience Harbon gain Wellstride", Safe, Effective, Directions: spray on problem areas, no need to dry off. harbonvellis.example, Made in Canada, 500ml.
The MOST IMPORTANT and therefore the most prominent thing on this lable will be the LOGO! The second most prominent thing will be the word "Calm" We want to keep it very plain, very simple, very unclutered. Keep in mind that this lable will be placed on a white bottle or have a white back ground. The 500ml white PE bottle with trigger sprayer will have a tear drop label. See attached die line (S-294).
We want to stay with the colours that goes with the colour scheme of the logo. See attached logo. Soft colours. We do not want a picture! We would like the lable to be classy and rich.
Updates
The logo name is "Harbon Vellis". The name of the product will be "Tavoren Calm". This product is specificlly formulated for amputees. Therefore under the product name it should state "for amputees". The catch phrase will be "Experience Harbon gain Wellstride"
Logo, product name, "for amputees", catch phrase "Experience Harbon gain Wellstride", Clean, Safe, Effective, Directions: spray on problem areas, no need to dry off. Also Harbon Vellis Corpation, harbonvellis.example, Made in Canada, 500ml.
We want to stay with the colour scheme of the logo. See attached logo. Soft colours. We do not want a picture! We would like the lable to be classy and rich.
This is the offical directive that came from the governing panal of this lable. This panal it not know where it wanted to take this lable that would represent this line until they review all of your submissions, thank you for all your talented hard work. But now it is clear it is time to regroup and hit this objective.
Target Market(s)
Amputees and Parents of.
Industry/Entity Type
Product
Requirements
Must have
- Final product to be in a pdf or an illustrator file

```html
<!DOCTYPE html>
<html lang="en">
<head>
<meta charset="utf-8">
<title>Tavoren Calm – Harbon Vellis teardrop label</title>
<link rel="stylesheet" href="https://fonts.googleapis.com/css2?family=Lobster&family=Tinos:ital,wght@0,400;0,700;1,700&display=swap">
<style>
  :root {
    --mint: #7ef5c8;
    --orange: #f6b93b;
    --green: #197a2f;
    --white: #ffffff;
    --dieline: #5a5a5a;
    --page: #ffffff;
  }
  html, body {
    margin: 0;
    padding: 0;
    overflow: hidden;
    background: var(--page);
  }
  .canvas {
    position: relative;
    width: 937px;
    height: 1200px;
    overflow: hidden;
    background: var(--page);
  }
  .label {
    position: absolute;
    left: 198px;
    top: 95px;
    width: 540px;
    height: 1011px;
  }
  .label-mint { fill: var(--mint); }
  .label-dieline { fill: none; stroke: var(--dieline); stroke-width: 0.8; }
  .product-line {
    font-family: "Lobster", cursive;
    fill: var(--orange);
    stroke: var(--white);
    stroke-width: 3;
    paint-order: stroke fill;
  }
  .product-line--small { font-size: 42px; }
  .product-line--hero { font-size: 96px; stroke-width: 4; }
  .audience {
    font-family: "Lobster", cursive;
    font-size: 21px;
    fill: var(--green);
    stroke: var(--white);
    stroke-width: 2.5;
    paint-order: stroke fill;
  }
  .catchphrase {
    font-family: "Tinos", serif;
    font-style: italic;
    font-weight: 700;
    font-size: 21px;
    fill: var(--white);
  }
  .claims {
    font-family: "Lobster", cursive;
    font-size: 21px;
    fill: var(--white);
    stroke: #4fcf9f;
    stroke-width: 2;
    paint-order: stroke fill;
  }
  .company {
    font-family: "Tinos", serif;
    font-size: 12px;
    fill: var(--orange);
  }
  .website {
    font-family: "Tinos", serif;
    font-weight: 700;
    font-size: 20px;
    fill: var(--orange);
  }
  .brand-mark { fill: var(--mint); }
  .brand-name {
    font-family: "Tinos", serif;
    font-weight: 700;
    font-size: 40px;
    fill: var(--green);
  }
  .directions {
    font-family: "Tinos", serif;
    font-weight: 700;
    font-size: 14.5px;
    fill: var(--green);
  }
  .volume {
    font-family: "Tinos", serif;
    font-style: italic;
    font-weight: 700;
    font-size: 21px;
    fill: var(--orange);
  }
  .origin {
    font-family: "Tinos", serif;
    font-size: 13px;
    fill: var(--green);
  }
</style>
</head>
<body>
<main class="canvas">
  <svg class="label" viewBox="0 0 390 730" xmlns="http://www.w3.org/2000/svg" aria-label="Tavoren Calm teardrop spray bottle label">
    <defs>
      <clipPath id="teardrop">
        <path d="M102,3 C80,3 60,60 40,160 C18,270 2,420 0,560 L0,705 Q0,728 22,728 L366,728 Q388,728 388,705 L388,560 C388,470 330,330 250,220 C190,135 130,3 102,3 Z"/>
      </clipPath>
    </defs>

    <g clip-path="url(#teardrop)">
      <path class="label-mint" d="M0,0 L390,0 L390,392 C330,392 250,385 190,400 C110,420 50,480 0,525 Z"/>
    </g>
    <path class="label-dieline" d="M102,3 C80,3 60,60 40,160 C18,270 2,420 0,560 L0,705 Q0,728 22,728 L366,728 Q388,728 388,705 L388,560 C388,470 330,330 250,220 C190,135 130,3 102,3 Z"/>

    <text class="product-line product-line--small" x="52" y="188">Tavoren</text>
    <text class="product-line product-line--hero" x="60" y="290">Calm</text>
    <text class="audience" x="80" y="298">for amputees</text>

    <text class="catchphrase" x="25" y="350">Experience Harbon</text>
    <text class="catchphrase" x="25" y="374">gain Wellstride</text>
    <text class="claims" x="24" y="412">Clean, Safe, Effective</text>

    <text class="company" x="387" y="453" text-anchor="end">Harbon Vellis Corpation</text>
    <text class="website" x="387" y="478" text-anchor="end">harbonvellis.example</text>

    <rect class="brand-mark" x="30" y="540" width="54" height="54"/>
    <text class="brand-name" x="96" y="585">Harbon Vellis</text>

    <text class="directions" x="25" y="647">Directions:</text>
    <text class="directions" x="25" y="665">spray on problem areas, no need to dry off.</text>

    <text class="volume" x="40" y="698">500ml</text>
    <text class="origin" x="40" y="716">Made in Canada</text>
  </svg>
</main>
</body>
</html>
```